Calm Fern Wellcare- Aged Care and Community Services

Looking for brochure to advertise our services. I will attach a draft that we do not want to use. Looking for graphics that are as natural as possible to present a personalised service. We supply services to aged people and people with disability. Please make it look classy and professional at the same time. I am looking for creativity. I have also attached the logo. Site addresses can be the last page. ideally looking for 2 designs, one A4 and another smaller possibly DL. Looking for creative out of the box thinkers. Thank you.

Target Market(s)

Aged Care service providers, disability service providers and private hospitals

Font styles to use
Serif
Sans Serif
Script

Colors
6b449b
886aae
eea4c8
f59195
fac994
3176b5
0555a3
cedeed
e4daeb

Requirements
Must have
• Targeted imagery, content and contact details
Nice to have
• personal profiles of people happy with our services

```html
<!DOCTYPE html>
<html lang="en">
<head>
<meta charset="utf-8">
<title>Calm Fern Wellcare – Brochure</title>
<link href="https://fonts.googleapis.com/css2?family=Fira+Sans:wght@400;500;600;700&display=swap" rel="stylesheet">
<style>
:root{
  --purple:#6b3fa3;
  --purple-dark:#54288c;
  --violet:#7d4bb0;
  --pink:#e8287f;
  --pink-soft:#ef4f95;
  --blue:#5e92d3;
  --blue-light:#c7d8ef;
  --lavender:#9b7ecd;
  --lavender-pale:#d9cbee;
  --grey-panel:#efeff1;
  --ink:#222;
  --page:#e6e6ea;
}
*{margin:0;padding:0;box-sizing:border-box}
html,body{width:881px;height:1200px;overflow:hidden;background:var(--page)}
body{font-family:"Fira Sans",Arial,sans-serif;color:var(--ink);position:relative}
.spread{position:absolute;left:74px;width:734px;height:519px;background:#fff;overflow:hidden}
.spread-front{top:56px}
.spread-back{top:620px}
.spread>svg{position:absolute;left:0;top:0}
.t{position:absolute;line-height:1.2}
.center{text-align:center}
.right{text-align:right}
.justify{text-align:justify}
.white{color:#fff}
.purple{color:var(--purple)}
.pink{color:var(--pink)}
.heading{font-weight:700;letter-spacing:.3px}
.body-small{font-size:6.6px;line-height:8.8px}
.label{font-size:7.3px;font-weight:600;color:var(--purple);text-align:center;line-height:9px}
.brand-name{font-size:21px;font-weight:600;color:var(--purple);letter-spacing:.3px;white-space:nowrap}
.phone-pill{position:absolute;height:32px;border-radius:16px;border:2px solid #fff;display:flex;align-items:center;justify-content:center;gap:8px;color:#fff;font-size:23px;font-weight:700;letter-spacing:1px}
.phone-pill svg{width:20px;height:20px}
.web{position:absolute;font-size:14px;font-weight:600;color:var(--purple);display:flex;align-items:center;gap:5px}
.web svg{width:12px;height:12px}
.bullets{font-size:6.2px;line-height:8.4px;font-weight:500;white-space:nowrap}
.bullets span{color:var(--pink)}
</style>
</head>
<body>

<section class="spread spread-front">
  <svg width="734" height="519" viewBox="0 0 734 519">
    <defs>
      <linearGradient id="topBand" x1="0" x2="1"><stop offset="0" stop-color="#5b2a8e"/><stop offset=".5" stop-color="#7d3aa3"/><stop offset=".52" stop-color="#e8287f"/><stop offset="1" stop-color="#e8287f"/></linearGradient>
      <linearGradient id="purpleSweep" x1="0" y1="0" x2="1" y2="1"><stop offset="0" stop-color="#6a35a6"/><stop offset="1" stop-color="#8a4fb5"/></linearGradient>
      <radialGradient id="photoCare" cx=".45" cy=".45" r=".75"><stop offset="0" stop-color="#f4e2da"/><stop offset=".45" stop-color="#e9d2c6"/><stop offset=".75" stop-color="#c9c3d6"/><stop offset="1" stop-color="#6f93c8"/></radialGradient>
      <radialGradient id="photoA" cx=".5" cy=".5" r=".6"><stop offset="0" stop-color="#e8ece6"/><stop offset="1" stop-color="#7fb2a0"/></radialGradient>
      <radialGradient id="photoB" cx=".5" cy=".45" r=".6"><stop offset="0" stop-color="#e4d25a"/><stop offset=".6" stop-color="#8a6a52"/><stop offset="1" stop-color="#c9cdd4"/></radialGradient>
      <radialGradient id="photoC" cx=".5" cy=".5" r=".6"><stop offset="0" stop-color="#f3efea"/><stop offset="1" stop-color="#b9a99a"/></radialGradient>
    </defs>
    <rect x="0" y="0" width="367" height="519" fill="var(--grey-panel)"/>
    <path d="M688 11 C718 40 700 75 712 105 C722 130 734 138 734 138 V11 Z" fill="var(--blue-light)"/>
    <path d="M0 11 H367 V98 Q260 160 182 149 Q70 138 0 100 Z" fill="var(--blue)"/>
    <path d="M0 355 C40 348 72 398 120 420 C158 437 182 458 182 480 H0 Z" fill="var(--blue-light)"/>
    <circle cx="63" cy="290" r="37" fill="url(#photoA)" stroke="var(--pink)" stroke-width="2.5" role="img" aria-label="Carer supporting an elderly resident"/>
    <circle cx="177" cy="320" r="37" fill="url(#photoB)" stroke="var(--pink)" stroke-width="2.5" role="img" aria-label="Smiling professional staff member"/>
    <circle cx="297" cy="285" r="37" fill="url(#photoC)" stroke="var(--pink)" stroke-width="2.5" role="img" aria-label="Trainer presenting at a staff training session"/>
    <rect x="368" y="156" width="366" height="254" fill="url(#photoCare)" role="img" aria-label="Carer smiling with an elderly woman"/>
    <path d="M193 479 C300 352 430 296 540 306 C625 313 690 360 734 402 V479 Z" fill="var(--pink)"/>
    <path d="M193 479 C300 362 430 308 540 318 C620 325 690 372 734 416 V479 Z" fill="url(#purpleSweep)"/>
    <rect x="0" y="479" width="734" height="40" fill="#fff"/>
    <rect x="0" y="0" width="734" height="11" fill="url(#topBand)"/>
    <path d="M351 354 a6 6 0 0 1 6 6 c0 5 -6 11 -6 11 s-6 -6 -6 -11 a6 6 0 0 1 6 -6 z" fill="var(--pink)"/>
    <circle cx="351" cy="360" r="2.2" fill="#7a44ad"/>
  </svg>

  <h2 class="t heading white" style="left:66px;top:19px;font-size:14px">PATIENT SATISFACTION</h2>
  <h3 class="t heading white" style="left:66px;top:39px;font-size:8px">THE REAL RETURN OF INVESTMENT</h3>
  <p class="t white body-small justify" style="left:66px;top:48px;width:293px">The more your clients are satisfied, the more they are capable of promoting your brand, speaking highly of your service delivery during accreditation’s and ultimately the more they feel you value them as individuals. The Care Standards Council relentlessly seek evidence and compassionate, compliant and efective corporate and clinical governance, by embeding these standards into each policy, proces, service implementation to evaluation, the more you will have peace of mind should any regulatory department decides to pay you a visit. We are here to ensure we align to your standards whilst being adaptable to the changing nature of the industry we operate in.</p>

  <h2 class="t heading center purple" style="left:0;width:367px;top:163px;font-size:13.5px"><span class="pink">REDESIGNING</span> RESIDENT EXPERIENCES</h2>
  <p class="t center" style="left:0;width:367px;top:181px;font-size:7.8px;line-height:10.5px">We value feedback and we consistently seek it as it helps us grow.<br>Service delivery &amp; feedback are a match that cannot be unwedded.</p>

  <h2 class="t heading center purple" style="left:0;width:356px;top:216px;font-size:13.5px;line-height:15px">RETAINING CUSTOMERS<br>&amp; HOW WE <span class="pink">GROW</span></h2>

  <p class="t label" style="left:13px;width:100px;top:334px">ENSURE POSITIVE<br>FIRST ENCOUNTER</p>
  <p class="t label" style="left:131px;width:100px;top:362px">MAINTAIN<br>PROFESSIONALISM</p>
  <p class="t label" style="left:243px;width:110px;top:329px;font-weight:500">CONTINUE TRAINING<br>&amp; DEVELOPMENT</p>

  <div class="t right" style="left:210px;width:147px;top:374px;font-size:6.8px;line-height:9px;color:#fff;font-weight:500">
    <p style="color:#f59ac4">PERTH ADDRESS</p>
    <p>14 Mossvale Lane<br>Dunmore WA 6100</p>
    <p style="color:#f59ac4;margin-top:6px">ADELAIDE ADDRESS</p>
    <p>Ground Floor, 8 Kestrel Street,<br>Glenholt SA 5070</p>
    <p style="margin-top:6px">✉ admin@calmfernwellcare.com.au</p>
  </div>

  <p class="t white" style="left:392px;top:367px;font-size:34px;font-weight:500;line-height:36px">Re-Imagining<br><span style="font-weight:700">HEALTHCARE</span></p>

  <div class="t" style="left:440px;top:96px;width:236px;display:flex;align-items:center;justify-content:center;gap:6px">
    <span style="width:10px;height:10px;border-radius:50%;background:var(--pink);display:block;flex:none"></span>
    <span class="brand-name">Calm Fern Wellcare</span>
  </div>

  <p class="t purple" style="left:21px;top:430px;font-size:20px;font-weight:600">Talk to Us!</p>

  <div class="phone-pill" style="left:53px;top:458px;width:255px;background:var(--pink)">
    <svg viewBox="0 0 24 24" fill="none" stroke="#fff" stroke-width="2.4" stroke-linecap="round"><path d="M5 3h4l2 5-3 2a12 12 0 0 0 6 6l2-3 5 2v4a2 2 0 0 1-2 2A18 18 0 0 1 3 5a2 2 0 0 1 2-2z"/></svg>08 5550 1234</div>
  <div class="phone-pill" style="left:422px;top:458px;width:255px;background:var(--purple-dark)">
    <svg viewBox="0 0 24 24" fill="none" stroke="#fff" stroke-width="2.4" stroke-linecap="round"><path d="M5 3h4l2 5-3 2a12 12 0 0 0 6 6l2-3 5 2v4a2 2 0 0 1-2 2A18 18 0 0 1 3 5a2 2 0 0 1 2-2z"/></svg>08 5550 1234</div>

  <p class="web" style="left:74px;top:493px"><svg viewBox="0 0 24 24" fill="none" stroke="var(--pink)" stroke-width="2.2"><circle cx="12" cy="12" r="10"/><path d="M2 12h20M12 2c3 3 3 17 0 20M12 2c-3 3-3 17 0 20"/></svg>calmfernwellcare.com.au</p>
  <p class="web" style="left:444px;top:493px"><svg viewBox="0 0 24 24" fill="none" stroke="var(--pink)" stroke-width="2.2"><circle cx="12" cy="12" r="10"/><path d="M2 12h20M12 2c3 3 3 17 0 20M12 2c-3 3-3 17 0 20"/></svg>calmfernwellcare.com.au</p>
</section>

<section class="spread spread-back">
  <svg width="734" height="519" viewBox="0 0 734 519">
    <defs>
      <linearGradient id="headBand" x1="0" y1="0" x2="1" y2="1"><stop offset="0" stop-color="#5a3a99"/><stop offset="1" stop-color="#7b49ad"/></linearGradient>
      <linearGradient id="footBand" x1="0" x2="1"><stop offset="0" stop-color="#5b2a8e"/><stop offset=".5" stop-color="#8a3aa0"/><stop offset="1" stop-color="#e8287f"/></linearGradient>
      <linearGradient id="photoTeam" x1="0" y1="0" x2="0" y2="1"><stop offset="0" stop-color="#f1ecf6"/><stop offset=".3" stop-color="#dcc1ad"/><stop offset=".65" stop-color="#a9826c"/><stop offset="1" stop-color="#4b4047"/></linearGradient>
    </defs>
    <rect x="0" y="0" width="734" height="11" fill="var(--pink)"/>
    <path d="M0 11 H367 V95 Q290 142 190 140 Q80 138 0 89 Z" fill="url(#headBand)"/>
    <rect x="367" y="11" width="367" height="110" fill="url(#headBand)"/>
    <path d="M367 78 C420 48 480 36 545 36 C620 36 690 62 734 92 V140 H367 Z" fill="#fff"/>
    <rect x="0" y="287" width="367" height="161" fill="url(#photoTeam)" role="img" aria-label="Group of smiling diverse care staff"/>
    <rect x="0" y="447" width="734" height="60" fill="var(--blue-light)"/>
    <rect x="366" y="427" width="368" height="21" fill="var(--lavender)"/>
    <rect x="0" y="507" width="734" height="12" fill="url(#footBand)"/>

    <rect x="86" y="434" width="192" height="28" rx="14" fill="var(--purple-dark)"/>
    <rect x="176" y="457" width="46" height="2" fill="var(--pink)"/>
    <circle cx="54" cy="462" r="40" fill="var(--pink)" stroke="#fff" stroke-width="4"/>
    <g fill="#fff"><circle cx="54" cy="448" r="6"/><circle cx="41" cy="452" r="5"/><circle cx="67" cy="452" r="5"/><path d="M42 472 q12 -22 24 0 z"/><path d="M31 472 q10 -18 20 0 z"/><path d="M57 472 q10 -18 20 0 z"/></g>
    <path d="M30 476 q2 12 14 14 M78 476 q-2 12 -14 14" fill="none" stroke="#fff" stroke-width="3" stroke-linecap="round"/>

    <circle cx="416" cy="53" r="25" fill="#a98bd0" stroke="#fff" stroke-width="3"/>
    <g fill="none" stroke="#fff" stroke-width="1.4"><circle cx="416" cy="44" r="6"/><path d="M404 60h24M416 50v10M406 60v6M416 60v6M426 60v6"/></g>
    <circle cx="652" cy="53" r="25" fill="#a98bd0" stroke="#fff" stroke-width="3"/>
    <g fill="none" stroke="#fff" stroke-width="1.4"><path d="M646 72V50l-8-8M652 72V40M658 72V52l8-8M640 60h-6"/><circle cx="637" cy="41" r="2"/><circle cx="652" cy="38" r="2"/><circle cx="667" cy="43" r="2"/></g>

    <rect x="414" y="194" width="260" height="20" rx="10" fill="var(--purple-dark)"/>
    <path d="M576 194 H664 a10 10 0 0 1 0 20 H576 a10 10 0 0 1 0 -20z" fill="var(--pink-soft)"/>

    <g>
      <circle cx="542" cy="269" r="42" fill="#5a3a9a"/>
      <circle cx="542" cy="357" r="42" fill="#7a4aa8"/>
      <circle cx="497" cy="313" r="42" fill="#e8338a"/>
      <circle cx="587" cy="313" r="42" fill="#e94f93"/>
      <circle cx="542" cy="313" r="26" fill="var(--lavender-pale)"/>
      <circle cx="542" cy="313" r="20" fill="#fff"/>
    </g>
    <g fill="none" stroke="#fff" stroke-width="1.5">
      <circle cx="542" cy="257" r="9"/><path d="M542 241v4M529 257h-4M559 257h-4M530 245l3 3M554 245l-3 3"/>
      <path d="M582 303l5 -2 5 2v7q0 6-5 8q-5-2-5-8z M584 309l2 2 4-4" stroke-width="1.6"/>
      <path d="M486 322v-12h4l4-8q3 0 2 4l-1 4h6q2 0 2 3l-2 8q-1 2-3 2h-12z M482 310v12"/>
      <circle cx="542" cy="356" r="3"/><circle cx="533" cy="368" r="3"/><circle cx="551" cy="368" r="3"/><path d="M542 360v4l-8 2M542 364l8 2"/>
    </g>
    <text x="542" y="260" text-anchor="middle" font-family="Fira Sans, sans-serif" font-size="9" font-weight="700" fill="#fff">$</text>
  </svg>

  <h2 class="t heading center white" style="left:0;width:352px;top:19px;font-size:14px">ABOUT US</h2>
  <p class="t white body-small justify" style="left:17px;top:41px;width:333px">Calm Fern Wellcare is a Perth based staffing solutions providers which thrives to partner with organisations in meeting their resource requirements. We are slowly building a reputation on our responsiveness to client enquiries, whilst meeting ourkey service deliverables. We work with service providers in Residential Aged Care,Comunity Supports and Hospitals.</p>
  <p class="t white body-small center" style="left:17px;top:85px;width:333px">We believe in the key to building lasting relationships in life to have a willingness and ability to resiprocity which we aim to do by understanding the intricate needs of our clients, collaboratively identify problems, help them progress from their current situation, earn trust &amp; thrive for excellence.</p>

  <h2 class="t heading center" style="left:0;width:352px;top:154px;font-size:17px;color:var(--purple)">OUR <span class="pink">VISION</span></h2>
  <p class="t center pink" style="left:0;width:352px;top:176px;font-size:7.8px;font-weight:600">Our vision is to be the most responsive staffing solutions provider in WA and SA.</p>
  <p class="t center" style="left:10px;width:332px;top:186px;font-size:7.8px;line-height:10.3px">We thrive to attract, hire,place and retain staff with natural values which include ethics, accountability, respect, integrity and adaptability.<br>We will unceasingly adapt to the changes in our environment to ensure we always meet, and at times exceed our partnership expectations.</p>

  <h2 class="t heading white" style="left:104px;top:440px;font-size:13px">WHAT WE BELIEVE</h2>
  <p class="t body-small justify" style="left:104px;top:473px;width:247px;font-size:6.2px">A person who is appreciated, always done more than what is expected. Our staff are at the centre of all our decisions as we are only as good as the people we hire. If we look after our staff, they will look after our client.</p>

  <h2 class="t heading center white" style="left:367px;width:367px;top:15px;font-size:13.5px">WHY PARTNER WITH US?</h2>
  <h3 class="t heading pink" style="left:443px;top:66px;font-size:9.5px;font-weight:600">SERVICE DESIGN</h3>
  <h3 class="t heading pink" style="left:560px;top:66px;font-size:9.5px;font-weight:600">TECHNOLOGY</h3>
  <p class="t body-small justify" style="left:378px;top:83px;width:154px">Prior to placing all staff, we ensure we have conducted a full client profile to understand your business needs, to end-to-end operations, service delivery, HR andgovernance. This will enable us to design a service around your specific needs which allows for a seamless integration. We encourage continuity of service delivery which we implement by ensuring the same staff are placed at your sites. Culturally, this enable our staf to build relationshipswith your team and customers allowing for a natural fit.</p>
  <p class="t body-small justify" style="left:543px;top:83px;width:171px">We have integrated our systems with necessary technology as we believe technology is a part of modern day efficiencies. People are our business and nothing can replace human relationships, interactions or connection, however to efficiently enhance these human related characteristics, technology helps us in maximising efficiencies and minimising error. Our on-boarding and scheduling platforms are automated, further solidifying compliance and managing risks.</p>

  <p class="t heading white" style="left:426px;top:197px;font-size:12.5px;font-weight:600">KEY PARTNERSHIP</p>
  <p class="t heading white" style="left:586px;top:197px;font-size:12.5px;font-weight:600">BENEFITS</p>

  <div class="t center" style="left:381px;width:110px;top:225px;font-size:6px;line-height:8px">
    <p style="font-size:7.8px;font-weight:600;color:var(--purple)">FINANCIAL</p>
    <p>A partnership with Calm Fern will enhance your margins and profitable allowing you to put more money towards initiatives that enables operational excellence.</p>
  </div>
  <div class="t center" style="left:599px;width:110px;top:239px;font-size:6px;line-height:8px">
    <p style="font-size:7.8px;font-weight:600;color:var(--pink);line-height:9.5px">RISK MANAGEMENT<br>ENHANCEMENTS</p>
    <p>You have the option of outsourcing workcover and cost</p>
  </div>
  <div class="t center" style="left:376px;width:122px;top:354px;font-size:6px;line-height:8px">
    <p style="font-size:7.8px;font-weight:600;color:var(--pink);line-height:9.5px">SERVICE DELIVERY<br>IMPROVEMENTS</p>
    <p>Enhanced customer choice and flexibility as well as improved customer outcomes</p>
  </div>
  <div class="t center" style="left:592px;width:122px;top:359px;font-size:6px;line-height:8px">
    <p style="font-size:7.8px;font-weight:600;color:var(--purple)">OPERATIONAL EFFICIENCIES</p>
    <p>Improved organisational efficiencies and optimisation of the workforce.</p>
  </div>

  <h2 class="t heading center" style="left:367px;width:356px;top:408px;font-size:14px;color:var(--purple)"><span class="pink">WHO</span> WE EMPLOY</h2>
  <p class="t center white" style="left:367px;width:367px;top:429px;font-size:6.6px;line-height:8.5px;font-weight:500">OUR DIVERSE DATABASE OF SKILLED STAFF GIVES YOU THE PEACE OF MIND,<br>YOU NEED TO DO WHAT YOU DO BEST, LOOK AFTER YOUR CUSTOMERS.</p>
  <p class="t center" style="left:367px;width:350px;top:452px;font-size:6.3px;line-height:8.4px">We actively source and recruit skills professionals with direct cultural fit to most of our clients.<br>These roles include but are not limited to:</p>
  <div class="t bullets" style="left:372px;top:473px"><p><span>•</span> Registered Nurses</p><p><span>•</span> Enroled Nurses</p><p><span>•</span> Nursing Assistants/Carers</p></div>
  <div class="t bullets" style="left:465px;top:473px"><p><span>•</span> Allied Health Assistants (Physiotherapy &amp; OT)</p><p><span>•</span> Chefs and Cooks (Healthcare experienced)</p><p><span>•</span> Catering Staff and Kitchen Hands</p></div>
  <div class="t bullets" style="left:617px;top:473px"><p><span>•</span> Cleaning and Domestic Assistants</p><p><span>•</span> Laundry Attendant and</p><p><span>•</span> Many more related professionals</p></div>
</section>

</body>
</html>
```